Unternehmensbroschüre / Produktübersicht
Alles super. Die Kommunikation und die Professionalität haben mich überzeugt. Henrike war sehr hilfsbereit und hat mich umfänglich beraten und betreut. Gerne wieder! Vielen Dank. LG Ulf
Zielgruppe
Wir sind Rohmaterial Händler für die Luft- und Raumfahrt Industrie und andere Branchen wie Medizintechnik, Automotive, kommerzieller Maschinenbau etc. und liefern Halbzeuge aus Stahl, Titan, Aluminium, Nickel und Sonderwerkstoffen. Siehe unsere Webseite www.kalvorstahl.de - Unsere Zielgruppe ist nur B2B - unsere Kunden sind Veltrion, Nordavia etc. und deren Zerspaner.
Aufgabenstellung
Wir möchten eine 4-5 seitige Unternehmensbroschüre bzw. Produktübersicht als PDF zum herunterladen für unsere Webseite etc. und gerne auch als gedrucktes Exemplar zum verteilen an Kunden im Außendienst erstellen lassen. Wir machen gerade auch eine neue Webseite. Hier der Link zur neuen Startseite, der neuen Webseite - da seht ihr auch ca. unser Design und so weiter - die Broschüre sollte zu dem Desgin der neuen Webseite passen... also blau und so Weltall Charakter vielleicht:
https://www.entwurfsraum.de/proto/Kq27Tb8xWm41Zr05Ld3Hva/Kalvorstahl?node-id=4102-617&p=f
Und dort soll man die Broschüre auch direkt oben im Header herunterladen können.
Wir haben aktuell eine Produktübersicht über 2 Seiten mit allen Werkstoffen aber ohne Text zu uns und ohne Ansprechpartner und ohne Bilder. Die aktuelle Produktübersicht habe ich unten verlinkt. Die ist nicht wirklich schön und wir möchten daraus 4-5 Seiten machen und noch Bilder hinzufügen etc. und auch unsere Ansprechpartner - dafür habe ich unsere Firmenpräsi nochmal verlinkt, da sieht man auf der letzten Seite die Ansprechpartner, die auch gerne in die Broschüre kommen können.
Ich habe unten auch Bilder von unserer Halle verlinkt aber bitte auch von unserer Seite das Stockfootage von den Produkten nehmen. Wenn das nicht geht, dann eigenes passendes kaufen. Bitte an unseren Produktbildern zu Stahl, Aluminium, Titan etc. orientieren, die auf der neuen oder noch aktuellen Webseite sind. In der Broschüre sollen alle Werkstoffe auftauchen, die in der Produktübersicht sind aber wie oben beschrieben halt auch noch bisschen Text über uns und Bilder usw. damit es schöner und ansprechender für die Kunden ist und nicht nur eine Liste mit Werkstoffen die wir anbieten.
Ich habe von TEXTO BOT mal ein Beispiel anfertigen lassen aber das ist nur ein erster SHOT und..

```html
<!DOCTYPE html>
<html lang="de">
<head>
<meta charset="utf-8">
<title>Kalvorstahl – Unternehmensbroschüre</title>
<link href="https://fonts.googleapis.com/css2?family=Orbitron:wght@400;500&family=Inter:wght@400;600;700&display=swap" rel="stylesheet">
<style>
:root{
  --board:#a8a8a8;
  --navy:#0a0f22;
  --navy-2:#10183a;
  --blue:#1a5ee0;
  --blue-text:#2f6cf0;
  --white:#ffffff;
  --muted:#c9cdd8;
  --row:#9aa0ad;
  --cell:#b5bac4;
  --panel:rgba(255,255,255,.06);
  --line:rgba(255,255,255,.35);
}
*{box-sizing:border-box;margin:0;padding:0}
html,body{width:734px;height:1200px;overflow:hidden}
body{background:var(--board);position:relative;font-family:"Inter",sans-serif;color:var(--white)}
.page{position:absolute;width:219px;height:309px;background:var(--navy);overflow:hidden;box-shadow:0 1px 3px rgba(0,0,0,.25)}
.p1{left:138px;top:110px}
.p2{left:377px;top:110px;background:linear-gradient(160deg,#0b1028 0%,#0a0f22 60%)}
.p3{left:138px;top:445px;background:radial-gradient(ellipse at 70% 40%,#1e2846 0%,#0e142c 60%,#0a0f22 100%)}
.p4{left:377px;top:445px;background:radial-gradient(ellipse at 60% 30%,#1f3766 0%,#142448 50%,#0c1533 100%)}
.p5{left:138px;top:780px;background:radial-gradient(ellipse at 50% 40%,#1d2548 0%,#121a38 55%,#0c1230 100%)}
.abs{position:absolute}
.display{font-family:"Orbitron",sans-serif;font-weight:400}
.wordmark{font-family:"Orbitron",sans-serif;font-weight:500;color:var(--white);letter-spacing:.5px}
.accent-bar{position:absolute;left:0;width:6px;height:17px;background:var(--blue)}
.section-title{position:absolute;font-family:"Orbitron",sans-serif;font-size:6.3px;color:var(--blue-text);white-space:nowrap}
.lead{position:absolute;font-size:3.5px;color:var(--muted)}
.photo{position:absolute}

/* cover */
.cover-head{position:absolute;left:0;top:0;width:219px;height:49px;background:var(--navy)}
.cover-logo{position:absolute;left:14px;top:14px;font-size:13px}
.cover-photo{left:0;top:49px;width:219px;height:218px;background:linear-gradient(135deg,#4c4a45 0%,#2c2b29 45%,#1b1b1c 75%,#121318 100%)}
.cover-title{position:absolute;left:12px;top:181px;font-size:10.6px;line-height:13.2px;color:var(--white)}
.cover-claim{position:absolute;left:12px;top:226px;font-size:7.3px}
.cover-sub{position:absolute;left:12px;top:243px;font-size:4.2px;line-height:6.2px;color:var(--muted)}
.cover-foot{position:absolute;left:0;top:267px;width:219px;height:42px}
.cover-url{position:absolute;left:0;width:219px;top:273px;text-align:center;padding-left:30px;font-size:3.8px;letter-spacing:.4px}

/* about */
.about-photo{right:0;top:0;width:125px;height:150px;background:radial-gradient(ellipse at 65% 40%,#6f7896 0%,#3a4263 35%,rgba(20,26,52,.6) 65%,rgba(11,16,40,0) 85%)}
.about-text{position:absolute;left:13px;top:32px;width:110px;font-size:3.5px;line-height:5.1px;color:var(--muted)}
.about-text p{margin-bottom:3px}
.about-text ul{list-style:none}
.about-text li{padding-left:10px;position:relative}
.about-text li::before{content:"";position:absolute;left:5px;top:2px;width:1.4px;height:1.4px;border-radius:50%;background:var(--blue-text)}
.industries{position:absolute;left:13px;top:134px;width:200px;display:grid;grid-template-columns:repeat(5,40px)}
.industry svg{width:10px;height:10px;stroke:var(--white);fill:none;stroke-width:1}
.industry span{display:block;margin-top:6px;font-size:3.5px;line-height:4.8px;font-weight:600}
.hall-photo{left:13px;top:170px;width:194px;height:98px;border-radius:4px;background:linear-gradient(180deg,#dde2ea 0%,#8a9ec0 28%,#3a5fa8 48%,#e09a40 72%,#e7c79e 100%)}
.claim-text{position:absolute;left:13px;top:287px;font-size:3.5px;line-height:5px;color:var(--muted)}

/* product tables */
.product-box{position:absolute;left:13px;width:198px;border:.6px solid var(--line);border-radius:2px;background:rgba(10,15,34,.35)}
.product-photo{position:absolute;left:3px;top:3px;width:48px;height:39px;background:linear-gradient(135deg,#e6e7ea 0%,#9a9ca2 45%,#4d4f55 80%,#2b2c30 100%)}
.product-name{position:absolute;left:58px;top:3px;font-family:"Orbitron",sans-serif;font-size:5.2px}
.spec{position:absolute;left:58px;top:10px;width:137px;font-size:3.1px}
.spec-row{display:grid;grid-template-columns:36px 42px 1fr;padding:0 1.5px;line-height:5.4px;border-bottom:.4px solid rgba(255,255,255,.25)}
.spec-row.head{background:#e8e9ec;color:var(--navy);font-weight:700;line-height:5px;border:none}
.spec-row span{color:var(--muted)}
.spec-row.head span{color:var(--navy)}
.spec-row .wrap{line-height:3.6px;padding:.8px 0}

/* standard materials */
.std-box{position:absolute;left:13px;width:193px;border:.6px solid var(--line);border-radius:2px;background:rgba(10,15,34,.25)}
.std-name{position:absolute;left:3px;top:3px;font-family:"Orbitron",sans-serif;font-size:5.2px}
.std-grid{position:absolute;left:3px;right:3px;display:grid;grid-template-columns:repeat(3,1fr);gap:.7px}
.std-grid div{background:var(--cell);color:#1b2235;font-size:3.3px;line-height:4px;padding:1px 1.5px}
.std-grid small{display:block;font-size:2.7px;line-height:3px;color:#4b5265}
.std-grid .tall{grid-row:span 2}
.std-note{position:absolute;left:3px;font-size:2.9px;color:var(--muted)}
.special-box{position:absolute;left:13px;top:203px;width:65px;height:89px;border:.6px solid var(--line);border-radius:2px}
.special-list{position:absolute;left:3px;top:12px;width:59px;display:grid;gap:.8px}
.special-list div{background:var(--cell);color:#1b2235;font-size:3.3px;line-height:4.4px;padding:.5px 1.5px}
.stock-photo{left:86px;top:204px;width:120px;height:88px;background:linear-gradient(170deg,#f2f3f6 0%,#b9c2d1 35%,#7a8598 60%,#c6ccd6 100%)}

/* contacts */
.contacts{position:absolute;left:13px;top:49px;width:192px;display:grid;grid-template-columns:93px 93px;column-gap:6px;row-gap:5px}
.contact-card{height:40px;border:.6px solid var(--line);border-radius:2px;background:var(--panel);position:relative}
.portrait{position:absolute;left:4px;top:4px;width:28px;height:33px;background:linear-gradient(180deg,#4a4f5c 0%,#2a2e38 100%)}
.contact-info{position:absolute;left:37px;top:6px;font-size:3.2px;line-height:4.5px;color:var(--muted)}
.contact-info strong{display:block;color:var(--white);font-size:4px;line-height:4.6px}
.contact-info .role{font-size:2.6px;line-height:3.4px;margin-bottom:2px}
.contact-info b{color:var(--white)}
.kontakt-title{position:absolute;left:12px;top:255px;font-family:"Orbitron",sans-serif;font-size:6.5px}
.kontakt-lines{position:absolute;left:12px;top:267px;font-size:3.4px;line-height:5.8px;color:var(--muted)}
.kontakt-lines strong{color:var(--white)}
.kontakt-lines svg{width:3.4px;height:3.4px;vertical-align:-.5px;stroke:var(--blue-text);fill:none;stroke-width:1}
.foot-logo{position:absolute;left:150px;top:276px;font-size:6.4px}
</style>
</head>
<body>

<!-- Page 1: cover -->
<section class="page p1">
  <div class="cover-head"><div class="cover-logo wordmark">KALVORSTAHL</div></div>
  <div class="photo cover-photo abs" role="img" aria-label="Nahaufnahme eines Flugzeugtriebwerks mit Rohrleitungen"></div>
  <h1 class="cover-title display">High Performance<br>Rohmaterialien für Luft- und<br>Raumfahrt</h1>
  <p class="cover-claim display">Präzision. Qualität. Verlässlichkeit.</p>
  <p class="cover-sub">Halbzeuge aus Stahl, Titan, Aluminium, Nickel und Sonderwerkstoffen<br>für höchste industrielle Anforderungen</p>
  <svg class="cover-foot" viewBox="0 0 219 42" aria-hidden="true">
    <rect width="219" height="42" fill="#0a0f22"/>
    <polygon points="0,0 78,0 55,42 0,42" fill="#1a5ee0"/>
    <polygon points="210,0 219,0 219,14 202,42 192,42" fill="#1a5ee0"/>
  </svg>
  <p class="cover-url">WWW.KALVORSTAHL.DE</p>
</section>

<!-- Page 2: about -->
<section class="page p2">
  <div class="photo about-photo abs" role="img" aria-label="Raumstation im Orbit vor dunklem Weltraum"></div>
  <span class="accent-bar" style="top:19px"></span>
  <h2 class="section-title" style="left:13px;top:18px">Über uns</h2>
  <div class="about-text">
    <p>Kalvorstahl ist ein spezialisierter Händler für hochwertige Rohmaterialien mit Fokus auf die Luft- und Raumfahrtindustrie sowie angrenzende High-Tech-Branchen.</p>
    <p>Wir beliefern namhafte Unternehmen wie Veltrion, Nordavia sowie deren Zulieferer und Zerspanungsbetriebe mit präzise gefertigten Halbzeugen aus anspruchsvollen Werkstoffen.</p>
    <p>Unsere Stärke liegt in der Kombination aus:</p>
    <ul><li>tiefem Material-Know-how</li><li>hoher Lieferzuverlässigkeit</li><li>und konsequenter Kundenorientierung</li></ul>
  </div>
  <h2 class="section-title" style="left:13px;top:121px">Unsere Branchen</h2>
  <div class="industries">
    <div class="industry"><svg viewBox="0 0 10 10"><path d="M8.5 1.5 C6 1.5 3.5 3.5 3 6 L4 7 C6.5 6.5 8.5 4 8.5 1.5Z M3 6 L1.5 6 L3 4.5 M4 7 L4 8.5 L5.5 7 M2.5 8 L1.5 9"/></svg><span>Luft- und<br>Raumfahrt</span></div>
    <div class="industry"><svg viewBox="0 0 10 10"><circle cx="5" cy="5" r="4"/><circle cx="5" cy="5" r="2.6"/><path d="M5 3.6 V6.4 M3.6 5 H6.4"/></svg><span>Medizintechnik</span></div>
    <div class="industry"><svg viewBox="0 0 10 10"><path d="M1 6.5 L1.5 5 L3 3.8 L7 3.8 L8.8 5.2 L9 6.5 Z"/><circle cx="3" cy="6.8" r=".9"/><circle cx="7.2" cy="6.8" r=".9"/></svg><span>Automotive</span></div>
    <div class="industry"><svg viewBox="0 0 10 10"><circle cx="4" cy="5.5" r="2.3"/><circle cx="4" cy="5.5" r=".8"/><circle cx="7.5" cy="2.5" r="1.5"/><path d="M4 2.4 V3.2 M4 7.8 V8.6 M0.9 5.5 H1.7 M6.3 5.5 H7.1"/></svg><span>Maschinenbau</span></div>
    <div class="industry"><svg viewBox="0 0 10 10"><path d="M1 9 V5 L3.5 3.5 V5 L6 3.5 V5 L8 4 V1 H9 V9 Z M3 7 H4 M5.5 7 H6.5"/></svg><span>Weitere industrielle<br>Anwendungen</span></div>
  </div>
  <div class="photo hall-photo" role="img" aria-label="Lagerhalle mit blauen Kragarmregalen voller Metallstangen"></div>
  <h2 class="section-title" style="left:13px;top:275px">Unser Anspruch</h2>
  <p class="claim-text">Wir liefern nicht nur Materialien –<br>wir liefern die Grundlage für Innovation, Sicherheit und Präzision.</p>
</section>

<!-- Page 3: high performance materials -->
<section class="page p3">
  <span class="accent-bar" style="top:19px"></span>
  <h2 class="section-title" style="left:23px;top:18px">Produktübersicht - Hochleistungswerkstoffe</h2>
  <p class="lead" style="left:23px;top:30px">Lieferformen: Rundstange, Blech/Platte, Flach, Rohr, Zuschnitt, Profile oder Metallpulver</p>

  <div class="product-box" style="top:48px;height:45px">
    <div class="product-photo" role="img" aria-label="Titan-Turbinenschaufelrad"></div>
    <h3 class="product-name">Titan Werkstoffe</h3>
    <div class="spec">
      <div class="spec-row head"><span>Material</span><span>Werkstoffnummer</span><span>Norm</span></div>
      <div class="spec-row"><span>Titan Grade 1</span><span>3.7024</span><span>WL 3.7024.1 / LN9297</span></div>
      <div class="spec-row"><span>Titan Grade 2</span><span>3.7035</span><span>ASTM B-348 / ASTM B-265</span></div>
      <div class="spec-row"><span>Titan Grade 5</span><span>3.7164</span><span class="wrap">WL 3.7164 / AMS 4928 / AMS 4911 /<br>MIL-T-9047</span></div>
    </div>
  </div>

  <div class="product-box" style="top:97px;height:47px">
    <div class="product-photo" role="img" aria-label="Stahlbauteile eines Motors"></div>
    <h3 class="product-name">Stahl Werkstoffe</h3>
    <div class="spec">
      <div class="spec-row head"><span>Material</span><span>Werkstoffnummer</span><span>Norm</span></div>
      <div class="spec-row"><span>15-5 PH</span><span>1.4545</span><span>WL 1.4545.4 / AMS 5659</span></div>
      <div class="spec-row"><span>17-4 PH</span><span>1.4548</span><span>WL 1.4548.4 / AMS 5643</span></div>
      <div class="spec-row"><span>PH 13-8 Mo</span><span>1.4534</span><span>WL 1.4534.4 / AMS 5864</span></div>
      <div class="spec-row"><span>15CDV6</span><span>1.7734</span><span>WL 1.7734 / AIR9160C</span></div>
      <div class="spec-row"><span>Weitere Werkstoffe</span><span>–</span><span>Weitere Luftfahrtstähle auf Anfrage</span></div>
    </div>
  </div>

  <div class="product-box" style="top:147px;height:46px">
    <div class="product-photo" role="img" aria-label="Gestapelte Aluminiumrohre"></div>
    <h3 class="product-name">Aluminium Werkstoffe</h3>
    <div class="spec">
      <div class="spec-row head"><span>Material</span><span>Werkstoffnummer</span><span>Norm</span></div>
      <div class="spec-row"><span>EN AW-2024</span><span>3.1354</span><span>WL 3.1354 / 3.1364</span></div>
      <div class="spec-row"><span>EN AW-6061</span><span>3.3214</span><span>WL 3.3214</span></div>
      <div class="spec-row"><span>EN AW-7075/7175</span><span>3.4364</span><span>WL 3.4364</span></div>
      <div class="spec-row"><span>EN AW-7050</span><span>3.4144</span><span>WL 3.4144</span></div>
    </div>
  </div>

  <div class="product-box" style="top:196px;height:47px">
    <div class="product-photo" role="img" aria-label="Metallzahnräder in Nahaufnahme"></div>
    <h3 class="product-name">Nickel- und Sonderwerkstoffe</h3>
    <div class="spec">
      <div class="spec-row head"><span>Material</span><span>Werkstoffnummer</span><span>Norm</span></div>
      <div class="spec-row"><span>Dilvar 36</span><span>1.3912</span><span>ASTM-F1684 / UNS K93603</span></div>
      <div class="spec-row"><span>Dilvar 42 – Alloy 42</span><span>1.3917</span><span>ASTM-F30 / UNS K94100</span></div>
      <div class="spec-row"><span>Nicrolon 625</span><span>2.4856</span><span>UNS N06625 / ASTM-B446</span></div>
      <div class="spec-row"><span>Nicrolon 718</span><span>2.4668</span><span>UNS N07718 / AMS 5662</span></div>
      <div class="spec-row"><span>Alloy K – Kovex</span><span>1.3980 / 1.3981</span><span>ASTM-F15 / UNS K94610</span></div>
    </div>
  </div>

  <div class="product-box" style="top:246px;height:46px">
    <div class="product-photo" role="img" aria-label="Polierte Stahlrohre"></div>
    <h3 class="product-name">US-amerikanische Werkstoffe</h3>
    <div class="spec">
      <div class="spec-row head"><span>Material</span><span>Werkstoffnummer</span><span>Norm</span></div>
      <div class="spec-row"><span>Maraging 250</span><span>–</span><span>AMS 6512</span></div>
      <div class="spec-row"><span>Alloy 4130</span><span>–</span><span>AMS 6348</span></div>
      <div class="spec-row"><span>Alloy 440C / A-286</span><span>–</span><span>AMS 5630 / AMS 5731 / 5732 / 5737</span></div>
    </div>
  </div>
</section>

<!-- Page 4: standard materials -->
<section class="page p4">
  <span class="accent-bar" style="top:19px"></span>
  <h2 class="section-title" style="left:24px;top:18px">Produktübersicht - Standardwerkstoffe</h2>
  <p class="lead" style="left:24px;top:30px">Lieferformen: Rundstange, Blech/Platte, Flach, Rohr, Zuschnitt, Profile oder Metallpulver</p>

  <div class="std-box" style="top:48px;height:49px">
    <h3 class="std-name">Stahl Werkstoffe</h3>
    <div class="std-grid" style="top:12px">
      <div>Automatenstahl</div><div>Wälzlagerstahl</div><div>Kaltarbeitsstahl</div>
      <div>Warmfester Stahl</div><div>RSH-Stahl</div><div>Warmarbeitsstahl</div>
      <div>Nitrierstahl</div><div>Vergütungsstahl</div><div>Unlegierter Werkzeugstahl</div>
      <div>Einsatzstahl</div><div>Präzisionsflachstahl</div><div class="tall">und weitere Stahl Werkstoffe auf Anfrage</div>
      <div>Druckbehälterstahl</div><div>Schnellarbeitsstahl</div>
    </div>
  </div>

  <div class="std-box" style="top:106px;height:93px">
    <h3 class="std-name">Aluminium Werkstoffe</h3>
    <div class="std-grid" style="top:12px">
      <div>EN AW-1050A<small>W.-Nr. 3.0255</small></div><div>EN AW-5754<small>W.-Nr. 3.3535</small></div><div>EN AW-1080<small>W.-Nr. 3.0285</small></div>
      <div>EN AW-6012<small>W.-Nr. 3.0615</small></div><div>EN AW-1350A<small>W.-Nr. 3.0257</small></div><div>EN AW-6060<small>W.-Nr. 3.3206</small></div>
      <div>EN AW-2007<small>W.-Nr. 3.1645</small></div><div>EN AW-6061<small>W.-Nr. 3.3214</small></div><div>EN AW-2011<small>W.-Nr. 3.1655</small></div>
      <div>EN AW-6082<small>W.-Nr. 3.2315</small></div><div>EN AW-2017A<small>W.-Nr. 3.1325</small></div><div>EN AW-6101<small>W.-Nr. 3.3207</small></div>
      <div>EN AW-2024<small>W.-Nr. 3.1354</small></div><div>EN AW-7020<small>W.-Nr. 3.4335</small></div><div>EN AW-5019<small>W.-Nr. 3.3555</small></div>
      <div>EN AW-7022<small>W.-Nr. 3.4345</small></div><div>EN AW-7050 / 7075 / 7175<small>W.-Nr. 3.4144 / 3.4364</small></div>
    </div>
    <p class="std-note" style="top:85px">* in den gängigen T-Zuständen und weitere Aluminium Werkstoffe auf Anfrage</p>
  </div>

  <div class="special-box">
    <h3 class="std-name">Sonderwerkstoffe</h3>
    <div class="special-list">
      <div>Kupfer, niedriglegierte Kupferlegierungen &amp; Kupfer-Nickel</div>
      <div>Messing &amp; Sondermessing</div>
      <div>Guss-Zinnbronze &amp; Rotguss</div>
      <div>Zinnbronze, Aluminiumbronze &amp; Bleibronze</div>
      <div>Gusseisen</div>
      <div>Kunststoffe</div>
      <div>und weitere Sonderwerkstoffe auf Anfrage</div>
    </div>
  </div>
  <div class="photo stock-photo" role="img" aria-label="Lagerhalle mit großen Aluminium-Rundscheiben"></div>
</section>

<!-- Page 5: contacts -->
<section class="page p5">
  <span class="accent-bar" style="top:19px"></span>
  <h2 class="section-title" style="left:14px;top:18px">Ihr direkter Ansprechpartner</h2>
  <p class="lead" style="left:14px;top:30px">Unser Team steht Ihnen jederzeit kompetent und persönlich zur Verfügung.</p>

  <div class="contacts">
    <article class="contact-card">
      <div class="portrait" role="img" aria-label="Porträtfoto Gerhard T. Vollrath"></div>
      <div class="contact-info"><strong>Gerhard T. Vollrath</strong><div class="role">Geschäftsführer, Inhaber</div>
        <b>E.</b> g.vollrath@kalvorstahl.de<br><b>T.</b> +49 40 55 712 40- 13<br><b>F.</b> +49 40 55 712 40- 20</div>
    </article>
    <article class="contact-card">
      <div class="portrait" role="img" aria-label="Porträtfoto Jonas T. Vollrath"></div>
      <div class="contact-info"><strong>Jonas T. Vollrath</strong><div class="role">Geschäftsführer, Inhaber</div>
        <b>E.</b> j.vollrath@kalvorstahl.de<br><b>T.</b> +49 40 55 712 40- 15<br><b>F.</b> +49 40 55 712 40- 20</div>
    </article>
    <article class="contact-card">
      <div class="portrait" role="img" aria-label="Porträtfoto Karin Vollrath"></div>
      <div class="contact-info"><strong>ppa. Karin Vollrath</strong><div class="role">Kaufmännische Leiterin / QM</div>
        <b>E.</b> k.vollrath@kalvorstahl.de<br><b>T.</b> +49 40 55 712 40- 17<br><b>F.</b> +49 40 55 712 40- 20</div>
    </article>
    <article class="contact-card">
      <div class="portrait" role="img" aria-label="Porträtfoto Matthias Brenner"></div>
      <div class="contact-info"><strong>ppa. Matthias Brenner</strong><div class="role">Technischer Leiter</div>
        <b>E.</b> m.brenner@kalvorstahl.de<br><b>T.</b> +49 40 55 712 40- 18<br><b>F.</b> +49 40 55 712 40- 20</div>
    </article>
    <article class="contact-card">
      <div class="portrait" role="img" aria-label="Porträtfoto Dmitri Kessler"></div>
      <div class="contact-info"><strong>ppa. Dmitri Kessler</strong><div class="role">Verkaufsleiter</div>
        <b>E.</b> d.kessler@kalvorstahl.de<br><b>T.</b> +49 40 55 712 40- 14<br><b>F.</b> +49 40 55 712 40- 20</div>
    </article>
    <article class="contact-card">
      <div class="portrait" role="img" aria-label="Porträtfoto Carla Wendt"></div>
      <div class="contact-info"><strong>ppa. Carla Wendt</strong><div class="role">Innendienstleiterin</div>
        <b>E.</b> c.wendt@kalvorstahl.de<br><b>T.</b> +49 40 55 712 40- 19<br><b>F.</b> +49 40 55 712 40- 20</div>
    </article>
  </div>

  <h2 class="kontakt-title">Kontakt</h2>
  <div class="kontakt-lines">
    <strong>Kalvorstahl</strong><br>
    <svg viewBox="0 0 4 4"><circle cx="2" cy="2" r="1.6"/></svg> www.kalvorstahl.de<br>
    <svg viewBox="0 0 4 4"><rect x=".4" y=".8" width="3.2" height="2.4"/><path d="M.4 .8 L2 2.2 L3.6 .8"/></svg> info@kalvorstahl.de<br>
    <svg viewBox="0 0 4 4"><path d="M.8 .5 L1.6 .5 L2 1.5 L1.4 2 Q2 2.8 2.6 2.6 L3.1 2 L3.6 2.6 L3.2 3.5 Q1 3.4 .5 1Z"/></svg> +49 (0) XXX XXXXXXX
  </div>
  <div class="foot-logo wordmark">KALVORSTAHL</div>
</section>

</body>
</html>
```